Menu redesign of existing iPhone app Lumora

We need a design upgrade for a footer menu of an iPhone app. We need to incorporate a new button for competitions/missions and it should be extremely modern and clean. The central button to create a Lumora cannot be too different as our current users are familiar with its usage.

I have attached screenshots of the curent newsfeed and menu.

Target Market(s)

Photography lovers/ design lovers

Font styles to use
Sans Serif

Requirements
Must have
• Lumora Button,
• Home button,
• My Profile button,
• Find friends button,
• Notifications button,
• Settings button,
• Missions/Competition Button
Nice to have
• Similar Lumora button as existing on the app

```html
<!DOCTYPE html>
<html lang="en">
<head>
<meta charset="utf-8">
<title>Lumora — feed with upload menu</title>
<link rel="stylesheet" href="https://fonts.googleapis.com/css2?family=Open+Sans:wght@400;600&display=swap">
<style>
  :root {
    --stage: #454a55;
    --status-green: #7cc142;
    --menu-dark: #2b2e33;
    --button-green: #3f8a2a;
    --button-ring: #8fc47a;
    --dim: rgba(20, 22, 26, 0.55);
    --modal: #ffffff;
    --modal-line: #e3e5e8;
    --label: #3d4a5c;
    --star: #d99a2b;
    --chat: #2f86c8;
    --icon-dark: #1e1f22;
  }
  html, body {
    margin: 0;
    width: 1200px;
    height: 900px;
    overflow: hidden;
    background: var(--stage);
    font-family: "Open Sans", sans-serif;
  }
  .app-screen {
    position: absolute;
    left: 376px;
    top: 52px;
    width: 448px;
    height: 795px;
    overflow: hidden;
  }
  .app-screen svg { display: block; width: 100%; height: 100%; }
  .status-text { font-size: 8px; fill: #fff; font-weight: 600; }
  .post-author { font-size: 11px; fill: rgba(255,255,255,0.75); font-weight: 600; }
  .post-time { font-size: 8px; fill: rgba(255,255,255,0.6); }
  .modal-action { font-size: 8px; letter-spacing: 0.8px; fill: var(--label); font-weight: 600; }
  .menu-label { font-size: 10px; fill: rgba(255,255,255,0.7); }
  .badge-count { font-size: 8px; fill: #fff; font-weight: 600; }
</style>
</head>
<body>
<main class="app-screen">
  <svg viewBox="0 0 320 568" xmlns="http://www.w3.org/2000/svg">
    <defs>
      <linearGradient id="feedPhotoTone" x1="0" y1="0" x2="1" y2="1">
        <stop offset="0" stop-color="#d9d4c8"/>
        <stop offset="0.5" stop-color="#c9a06a"/>
        <stop offset="1" stop-color="#b5895a"/>
      </linearGradient>
    </defs>

    <!-- feed photo -->
    <rect class="feed-photo" x="0" y="0" width="320" height="568" fill="url(#feedPhotoTone)" role="img" aria-label="Photo of an olive wood cutting board on a worn white tiled table with herbs"/>

    <!-- post header -->
    <circle class="author-avatar" cx="28" cy="62" r="13" fill="#8a6f5c" role="img" aria-label="Author profile photo"/>
    <text class="post-author" x="48" y="60">Daniel Harrow</text>
    <text class="post-time" x="48" y="72">3 hours ago</text>

    <!-- post badges -->
    <circle cx="252" cy="42" r="12" fill="var(--star)"/>
    <path d="M252 35 l2.1 4.4 4.8 .6 -3.5 3.3 .9 4.8 -4.3-2.3 -4.3 2.3 .9-4.8 -3.5-3.3 4.8-.6z" fill="#fff"/>
    <circle cx="288" cy="38" r="12" fill="var(--chat)"/>
    <path d="M281 32 h14 a2 2 0 0 1 2 2 v7 a2 2 0 0 1-2 2 h-8 l-4 3 v-3 h-2 a2 2 0 0 1-2-2 v-7 a2 2 0 0 1 2-2z" fill="#fff"/>
    <text class="badge-count" x="288" y="40.5" text-anchor="middle" style="fill:var(--chat)">3</text>

    <!-- dim overlay -->
    <rect x="0" y="0" width="320" height="568" fill="var(--dim)"/>

    <!-- status bar -->
    <rect class="status-bar" x="0" y="0" width="320" height="18" fill="var(--status-green)"/>
    <g fill="#fff">
      <circle cx="8" cy="9" r="2"/><circle cx="13.5" cy="9" r="2"/><circle cx="19" cy="9" r="2"/>
      <circle cx="24.5" cy="9" r="2" fill="none" stroke="#fff" stroke-width="0.7"/>
      <circle cx="30" cy="9" r="2" fill="none" stroke="#fff" stroke-width="0.7"/>
    </g>
    <text class="status-text" x="36" y="12">NOVACELL</text>
    <path d="M82 8 a6 6 0 0 1 8 0 M84 10 a3 3 0 0 1 4 0" stroke="#fff" stroke-width="1" fill="none"/>
    <text class="status-text" x="160" y="12" text-anchor="middle">11:27 AM</text>
    <text class="status-text" x="278" y="12" text-anchor="end">100%</text>
    <rect x="282" y="5" width="24" height="8" rx="1.5" fill="none" stroke="#fff" stroke-width="0.8"/>
    <rect x="283.5" y="6.5" width="21" height="5" fill="#fff"/>
    <rect x="306.5" y="7.5" width="1.5" height="3" fill="#fff"/>

    <!-- bottom menu -->
    <circle class="menu-arc" cx="160" cy="600" r="140" fill="var(--menu-dark)"/>

    <g class="menu-button download">
      <circle cx="48" cy="510" r="22" fill="var(--button-ring)" opacity="0.6"/>
      <circle cx="48" cy="510" r="18" fill="var(--button-green)"/>
      <path d="M48 500 v12 M42 506 l6 6 6-6 M39 518 h18" stroke="#fff" stroke-width="2.6" fill="none" stroke-linecap="round"/>
    </g>
    <g class="menu-button home">
      <circle cx="272" cy="510" r="22" fill="var(--button-ring)" opacity="0.6"/>
      <circle cx="272" cy="510" r="18" fill="var(--button-green)"/>
      <path d="M272 499 l-11 10 h3 v9 h6 v-6 h4 v6 h6 v-9 h3z" fill="#fff"/>
    </g>

    <g class="menu-button missions">
      <circle cx="95" cy="481" r="15" fill="var(--button-ring)" opacity="0.6"/>
      <circle cx="95" cy="481" r="12" fill="var(--button-green)"/>
      <path d="M89 474 h12 v4 a6 6 0 0 1-12 0z M95 484 v4 M91 489 h8" stroke="#fff" stroke-width="1.8" fill="none" stroke-linecap="round"/>
      <path d="M89 475 h-3 a3 3 0 0 0 3 4 M101 475 h3 a3 3 0 0 1-3 4" stroke="#fff" stroke-width="1.2" fill="none"/>
    </g>
    <g class="menu-button notifications">
      <circle cx="225" cy="481" r="15" fill="var(--button-ring)" opacity="0.6"/>
      <circle cx="225" cy="481" r="12" fill="var(--button-green)"/>
      <path d="M219 485 v-5 a6 6 0 0 1 12 0 v5 l2 2 h-16z" fill="#fff"/>
      <circle cx="225" cy="489" r="1.8" fill="#fff"/>
    </g>

    <g class="menu-button create">
      <circle cx="160" cy="478" r="38" fill="var(--button-ring)" opacity="0.6"/>
      <circle cx="160" cy="478" r="32" fill="var(--button-green)"/>
      <path d="M160 459 l19 13.8 -7.3 22.2 h-23.4 l-7.3-22.2z" fill="#c9d2c4"/>
    </g>
    <text class="menu-label" x="160" y="532" text-anchor="middle">Lumora</text>

    <g class="menu-button profile">
      <circle cx="112" cy="552" r="11" fill="var(--button-green)"/>
      <circle cx="112" cy="549" r="3" fill="#fff"/>
      <path d="M106 558 a6 5 0 0 1 12 0z" fill="#fff"/>
    </g>
    <g class="menu-button find-friends">
      <circle cx="144" cy="552" r="11" fill="var(--button-green)"/>
      <circle cx="141" cy="549" r="2.6" fill="#fff"/>
      <circle cx="148" cy="549" r="2.6" fill="#fff"/>
      <path d="M136 557 a5 4 0 0 1 10 0z M143 557 a5 4 0 0 1 10 0z" fill="#fff"/>
    </g>
    <g class="menu-button settings">
      <circle cx="176" cy="552" r="11" fill="var(--button-green)"/>
      <circle cx="176" cy="552" r="5" fill="none" stroke="#fff" stroke-width="3" stroke-dasharray="2 1.6"/>
      <circle cx="176" cy="552" r="2.6" fill="none" stroke="#fff" stroke-width="1.4"/>
    </g>
    <g class="menu-button more">
      <circle cx="208" cy="552" r="11" fill="var(--button-green)"/>
      <circle cx="203" cy="552" r="1.5" fill="#fff"/>
      <circle cx="208" cy="552" r="1.5" fill="#fff"/>
      <circle cx="213" cy="552" r="1.5" fill="#fff"/>
    </g>

    <!-- upload chooser -->
    <g class="upload-chooser">
      <rect x="34" y="270" width="252" height="112" rx="2" fill="var(--modal)"/>
      <path d="M272 277 v8 M268 281 h8" stroke="#555" stroke-width="1"/>
      <line x1="34" y1="352" x2="286" y2="352" stroke="var(--modal-line)"/>
      <line x1="160" y1="352" x2="160" y2="382" stroke="var(--modal-line)"/>
      <rect x="73" y="298" width="48" height="36" rx="2" fill="var(--icon-dark)"/>
      <rect x="77" y="302" width="40" height="28" fill="#fff"/>
      <path d="M77 330 l12-14 9 9 6-5 13 10z" fill="var(--icon-dark)"/>
      <circle cx="108" cy="308" r="3.5" fill="var(--icon-dark)"/>
      <rect x="199" y="298" width="48" height="36" rx="2" fill="var(--icon-dark)"/>
      <g fill="#fff">
        <rect x="202" y="301" width="5" height="4"/><rect x="211" y="301" width="5" height="4"/><rect x="220" y="301" width="5" height="4"/><rect x="229" y="301" width="5" height="4"/><rect x="238" y="301" width="5" height="4"/>
        <rect x="202" y="327" width="5" height="4"/><rect x="211" y="327" width="5" height="4"/><rect x="220" y="327" width="5" height="4"/><rect x="229" y="327" width="5" height="4"/><rect x="238" y="327" width="5" height="4"/>
        <path d="M217 309 l13 7 -13 7z"/>
      </g>
      <text class="modal-action" x="97" y="370" text-anchor="middle">SELECT</text>
      <text class="modal-action" x="223" y="370" text-anchor="middle">CANCEL</text>
    </g>
  </svg>
</main>
</body>
</html>
```